Need web redesign for cybersecurity startup whose mission is to make robust cybersecurity protection

We need a web redesign for Velnastra, a cyber security startup. We already have a logo and website but we’re looking for a redesign to reflect the new messaging and positioning of the company – and to update our look with a more polished feel. We’re looking for clean, powerful, confident designs that easily communicate the problems within the cybersecurity space and how Velnastra is the answer to those problems.

We can have the long-scrolling stripe layout for the home page, but we don’t want a bunch of interior pages with the same long-scroll format. We’d like to do something a little different and easier to navigate.

Velnastra’s products simplify and automate cybersecurity defense so non-experts can successfully protect their information and focus on their business. Velnastra’s mission is to provide proactive cybersecurity protection that is easy to use, easy to implement and easy to afford. The designs should reflect this populist message as well as confidence and maybe a little irreverence. Additional key words to describe the company are: secure, protection, easy, everyone.

Velnastra offers multiple security products which can both be purchased directly from their site. They provide the world’s most widely used WAF rule set for Quellwarden as well as Velnastra Guarded Linux (VGL) and Velnastra Guarded Linux Kernels to protect Linux servers, IoT devices and Kestrabox containers.

Target Market(s)

IT leaders in small and mid-sized businesses, hosting providers, and enterprise dev ops, product and security groups

Industry/Entity Type

Security

Number of Pages Required

5+ page

Font styles to use
Serif
Sans Serif

Requirements
Must have
• - We can have the long-scrolling stripe layout for the home page, but we don’t want a bunch of interior pages with the same long-scroll format. We’d like to do something a little different and easier to navigate.
• - Clean, powerful, confident designs
• - Real imagery coupled with line designs
Nice to have
• Specific icons to be used for all marketing and web materials for each product:
• - Brindle Guard for Linux (BG/L)
• - QuellWarden Rules
• - Velnastra Guarded Linux Kernels
• - PRAVT - Commercial Support
• - Shielded OS for Kestrabox
• - Shielded Apps for Kestrabox
Should not have
• - No typical imagery for cybersecurity such as binary code, hooded figures, etc.

```html
<!DOCTYPE html>
<html lang="en">
<head>
<meta charset="utf-8">
<title>Velnastra — Linux Server Protection</title>
<link href="https://fonts.googleapis.com/css2?family=Open+Sans:wght@300;400;600;700&display=swap" rel="stylesheet">
<style>
:root{
  --ink:#2b2b2b;
  --muted:#8a8a8a;
  --soft:#f2f2f2;
  --line:#d4d4d4;
  --dark:#2a231f;
  --dark-2:#3d332c;
  --white:#ffffff;
  --accent:#c8102e;
  --body:'Open Sans', Arial, sans-serif;
}
*{box-sizing:border-box;margin:0;padding:0}
html,body{width:1200px;height:4265px;overflow:hidden;background:var(--white)}
body{font-family:var(--body);color:var(--ink);position:relative}
.band{position:absolute;left:0;width:1200px}
.center{text-align:center}
.section-title{font-weight:300;font-size:30px;letter-spacing:.5px;color:var(--ink)}
.lede{font-size:11.5px;line-height:19px;color:var(--muted);max-width:920px;margin:0 auto}

/* hero */
.hero{top:0;height:603px;background:linear-gradient(180deg,#4a4038 0%,#2f2924 55%,#1f1b18 100%)}
.hero .photo{position:absolute;inset:0;background:radial-gradient(ellipse at 65% 40%,rgba(120,104,90,.55),rgba(20,18,16,0) 60%)}
.brand{position:absolute;left:0;right:0;top:160px;display:flex;flex-direction:column;align-items:center;gap:8px}
.brand .dot{width:40px;height:40px;border-radius:50%;background:var(--accent)}
.brand .name{font-weight:700;font-size:15px;letter-spacing:1px;color:var(--white)}
.hero h1{position:absolute;top:262px;left:0;right:0;text-align:center;font-weight:300;font-size:48px;color:var(--white);letter-spacing:.5px}
.hero .sub{position:absolute;top:350px;left:0;right:0;text-align:center;font-weight:300;font-size:22px;color:#e4e4e4}
.play{position:absolute;border-radius:50%;background:rgba(255,255,255,.85);display:flex;align-items:center;justify-content:center}
.hero .play{width:40px;height:40px;left:580px;top:415px}

/* intro */
.intro{top:603px;height:335px}
.intro .section-title{margin-top:52px}
.intro .lede{margin-top:20px}
.tags{display:flex;justify-content:center;gap:18px;margin-top:42px}
.tag{border:1px solid #555;border-radius:3px;height:36px;padding:0 30px;font-size:13px;line-height:34px;color:var(--ink)}

/* services */
.services{top:938px;height:768px;background:var(--soft)}
.services .section-title{margin-top:48px}
.service-grid{position:absolute;top:132px;left:100px;width:1000px;display:grid;grid-template-columns:repeat(3,1fr);row-gap:58px}
.service{text-align:center;padding:0 40px}
.service svg{height:38px;width:38px}
.service h3{font-size:12.5px;font-weight:600;letter-spacing:.3px;margin-top:20px;text-transform:uppercase}
.service p{font-size:10.5px;line-height:16px;color:var(--muted);margin-top:12px}
.customers{position:absolute;top:555px;left:0;right:0}
.logo-row{display:flex;justify-content:center;align-items:center;gap:46px;margin-top:38px}
.customer{display:flex;align-items:center;gap:8px;font-size:20px;font-weight:400;color:#555}
.customer i{display:block;width:16px;height:16px;background:#777}

/* video */
.video{top:1706px;height:532px}
.video .section-title{margin-top:44px}
.video .frame{position:absolute;left:299px;top:120px;width:603px;height:333px;background:linear-gradient(135deg,#8b7a6a,#3f352d 55%,#b9ab9b)}
.video .play{width:58px;height:58px;left:272px;top:137px;background:rgba(255,255,255,.25);border:2px solid #fff}

/* testimonials */
.quote{background:linear-gradient(180deg,var(--dark-2),var(--dark));color:var(--white)}
.quote blockquote{position:absolute;left:150px;right:150px;text-align:center;font-size:17px;font-weight:300;line-height:26px;color:#eee}
.quote cite{position:absolute;left:0;right:0;text-align:center;font-style:normal;font-size:13px;color:#cfcfcf}
.quote-one{top:2238px;height:336px}
.quote-one blockquote{top:118px}
.quote-one cite{top:196px}
.quote-two{top:2980px;height:333px}
.quote-two blockquote{top:118px}
.quote-two cite{top:202px}

/* containers */
.containers{top:2574px;height:406px}
.containers .section-title{margin-top:50px}
.containers .lede{margin-top:18px;max-width:860px}
.audience{position:absolute;top:240px;left:0;right:0}
.aud{position:absolute;width:220px;margin-left:-110px;text-align:center}
.aud svg{width:50px;height:40px}
.aud span{display:block;margin-top:18px;font-size:17px;font-weight:300;color:#444}

/* news */
.news{top:3313px;height:512px}
.news h2{position:absolute;font-weight:300;font-size:28px}
.recent{position:absolute;left:134px;top:119px}
.item{display:flex;gap:20px;margin-bottom:17px;height:103px}
.thumb{width:131px;height:103px;flex:none}
.item h4{font-weight:400;font-size:19px;line-height:28px;width:240px;margin-top:6px}
.date{font-size:9.5px;font-weight:700;color:#444;margin-top:6px}
.feature{position:absolute;left:591px;top:125px;width:475px}
.feature .thumb{width:475px;height:222px;background:linear-gradient(135deg,#2d3b52,#0e1420 60%,#5a4a35)}
.feature h4{font-weight:400;font-size:19px;margin-top:8px}
.feature p{font-size:10.5px;line-height:16px;color:var(--muted);margin-top:6px}

/* tweet */
.tweet{top:3825px;height:148px;background:var(--dark)}
.tweet .bird{position:absolute;left:168px;top:52px;width:40px;height:40px;border-radius:50%;background:#4a403a}
.tweet p{position:absolute;left:267px;width:825px;top:33px;text-align:center;font-size:15px;line-height:28px;color:#e6e6e6;font-weight:300}

/* footer */
.footer{top:3973px;height:292px}
.f-brand{position:absolute;left:128px;top:44px;display:flex;flex-direction:column;align-items:center;gap:6px}
.f-brand .dot{width:40px;height:40px;border-radius:50%;background:var(--accent)}
.f-brand .name{font-weight:700;font-size:13px;letter-spacing:.8px}
.socials{position:absolute;left:134px;top:154px;display:flex;gap:8px}
.socials i{display:block;width:28px;height:28px;border-radius:50%;border:1.5px solid #333}
.f-col{position:absolute;top:40px}
.f-col h5{font-weight:400;font-size:14px;letter-spacing:.5px}
.f-col ul{list-style:none;margin-top:16px}
.f-col li{font-size:11px;line-height:19px;color:#444}
.sitemap{left:387px}
.newsletter{left:572px;width:200px}
.newsletter p{font-size:10.5px;line-height:19px;color:#444;margin-top:16px}
.newsletter .field{margin-top:14px;height:36px;border:1px solid var(--line);font-size:10px;padding:0 10px;line-height:34px;color:#666}
.newsletter .btn{margin-top:22px;display:inline-block;background:#1f1a17;color:#fff;font-size:10px;padding:6px 12px;font-weight:600}
.contact{left:890px}
.contact li{display:flex;gap:12px;align-items:flex-start;line-height:15px;margin-bottom:10px}
.contact svg{width:12px;height:12px;flex:none;margin-top:1px}
.copy{position:absolute;left:128px;right:128px;top:253px;border-top:1px solid var(--line);padding-top:10px;text-align:center;font-size:10px;color:#666}
</style>
</head>
<body>

<header class="band hero">
  <div class="photo" role="img" aria-label="Photo of a bearded man in a dark jacket standing in an office"></div>
  <div class="brand"><span class="dot"></span><span class="name">VELNASTRA ®</span></div>
  <h1>Don’t Be the Next Cyber Victim</h1>
  <p class="sub">Harden Your Shell Now</p>
  <div class="play"><svg width="14" height="16" viewBox="0 0 14 16"><path d="M2 1l11 7-11 7z" fill="#333"/></svg></div>
</header>

<section class="band intro center">
  <h2 class="section-title">Linux Server Protection for Everyone and Everything</h2>
  <p class="lede">Cyber attacks happen. The question is, are you ready? For too many mid-sized and small businesses the answer is no because they don’t think cyber protection is within reach. Even enterprises often are left unprotected by outdated endpoint protection or none at all. Velnastra protects Linux servers, web application servers, IoT devices and even Kestrabox containers. And, it just takes a couple of clicks for complete protection.</p>
  <div class="tags">
    <span class="tag">WAF Rules</span>
    <span class="tag">Linux Servers</span>
    <span class="tag">IoT Devices</span>
    <span class="tag">Kestrabox Containers</span>
  </div>
</section>

<section class="band services center">
  <h2 class="section-title">Our Services</h2>
  <div class="service-grid">
    <div class="service">
      <svg viewBox="0 0 40 40"><g fill="none" stroke="#222" stroke-width="5"><rect x="4" y="4" width="18" height="12" rx="6" transform="rotate(45 13 10)"/><rect x="18" y="22" width="18" height="12" rx="6" transform="rotate(45 27 28)"/></g><path d="M15 15l10 10" stroke="#222" stroke-width="4"/></svg>
      <h3>Brindle Guard for Linux</h3>
      <p>Guard your hosts in minutes, with rules that update on their own every day.</p>
    </div>
    <div class="service">
      <svg viewBox="0 0 40 40"><g fill="none" stroke="#222" stroke-width="3"><circle cx="13" cy="7" r="4"/><circle cx="27" cy="7" r="4"/><circle cx="13" cy="33" r="4"/><path d="M13 11v18M27 11c0 10-14 8-14 18"/></g></svg>
      <h3>QuellWarden Rules</h3>
      <p>The most widely used WAF rule set, tuned to stop attacks before they land.</p>
    </div>
    <div class="service">
      <svg viewBox="0 0 40 40"><g fill="#222"><circle cx="15" cy="24" r="11"/><circle cx="30" cy="10" r="7"/></g><circle cx="15" cy="24" r="4" fill="#f2f2f2"/><circle cx="30" cy="10" r="2.5" fill="#f2f2f2"/></svg>
      <h3>Velnastra Guarded Linux Kernels</h3>
      <p>Hardened kernels that block exploits and keep your servers steady and safe.</p>
    </div>
    <div class="service">
      <svg viewBox="0 0 40 40"><path d="M4 8h22a3 3 0 013 3v10a3 3 0 01-3 3H14l-7 6v-6H4a3 3 0 01-3-3V11a3 3 0 013-3z" fill="#222"/><path d="M32 15h4a3 3 0 013 3v9a3 3 0 01-3 3h-2v5l-6-5H18" fill="#222"/></svg>
      <h3>PRAVT - Commercial Support</h3>
      <p>Real people ready to help you set up, tune and run your protection stack.</p>
    </div>
    <div class="service">
      <svg viewBox="0 0 40 40"><path d="M12 18v-5a8 8 0 0116 0v5" fill="none" stroke="#222" stroke-width="4"/><rect x="8" y="18" width="24" height="18" rx="2" fill="#222"/></svg>
      <h3>Shielded OS for Kestrabox</h3>
      <p>A secure host layer that guards every container running on your machine.</p>
    </div>
    <div class="service">
      <svg viewBox="0 0 40 40"><rect x="9" y="3" width="22" height="34" rx="3" fill="none" stroke="#222" stroke-width="3"/><circle cx="20" cy="32" r="1.8" fill="#222"/></svg>
      <h3>Shielded Apps for Kestrabox</h3>
      <p>Protect the apps inside your containers with no change to your workflow.</p>
    </div>
  </div>
  <div class="customers">
    <h2 class="section-title">More than 20,000 servers protected</h2>
    <div class="logo-row">
      <span class="customer"><i></i>Cobaltia</span>
      <span class="customer">Rennmark</span>
      <span class="customer">Harbor Isle</span>
      <span class="customer">Southmere University</span>
      <span class="customer"><i></i>Tallpeak</span>
    </div>
  </div>
</section>

<section class="band video center">
  <h2 class="section-title">Harden Your Shell Now</h2>
  <div class="frame" role="img" aria-label="Video still of a cat sitting in a cardboard box">
    <div class="play"><svg width="18" height="20" viewBox="0 0 14 16"><path d="M2 1l11 7-11 7z" fill="#fff"/></svg></div>
  </div>
</section>

<section class="band quote quote-one" role="img" aria-label="Dark close-up photo of an eye with a circuit ring overlay">
  <blockquote>“We trust our server security to Velnastra Guarded Linux because it works. We’ve used it for years and it has been essential in keeping dark forces at bay.”</blockquote>
  <cite>Corwin Halsey, Pale Heron</cite>
</section>

<section class="band containers center">
  <h2 class="section-title">Yes. You Can Secure Kestrabox Containers</h2>
  <p class="lede">Kestrabox is the fastest growing application developer software in the world. But, people don’t realize that their containers are wide open to cyber attacks. Velnastra provides a secure OS kernel that is inherited by all containers on a single server. It’s easy to install, doesn’t impact performance and protects your containers against malicious attack immediately.</p>
  <div class="audience">
    <div class="aud" style="left:216px"><svg viewBox="0 0 50 40"><g fill="#222"><rect x="6" y="2" width="38" height="10"/><rect x="6" y="15" width="38" height="10"/><rect x="6" y="28" width="38" height="10"/></g><g fill="#fff"><circle cx="38" cy="7" r="1.5"/><circle cx="38" cy="20" r="1.5"/><circle cx="38" cy="33" r="1.5"/></g></svg><span>Hosting Providers</span></div>
    <div class="aud" style="left:458px"><svg viewBox="0 0 50 40"><path d="M6 4v32h40" fill="none" stroke="#222" stroke-width="3"/><path d="M9 34l9-16 8 8 8-14 10 22z" fill="#222"/></svg><span>Enterprises</span></div>
    <div class="aud" style="left:765px"><svg viewBox="0 0 50 40"><path d="M18 9V5h14v4" fill="none" stroke="#222" stroke-width="3"/><rect x="4" y="9" width="42" height="28" rx="3" fill="#222"/><rect x="22" y="18" width="6" height="5" fill="#fff"/></svg><span>Mid-sized &amp; Small Business</span></div>
    <div class="aud" style="left:1024px"><svg viewBox="0 0 50 40"><rect x="9" y="7" width="32" height="22" fill="none" stroke="#222" stroke-width="3"/><path d="M3 33h44" stroke="#222" stroke-width="4"/></svg><span>IoT OEMs</span></div>
  </div>
</section>

<section class="band quote quote-two" role="img" aria-label="Silhouettes of office workers against a city skyline">
  <blockquote>“Velnastra eliminated 80% of our shared server issues overnight. And, it saves us about four hours of staff time every day because it protects servers automatically.”</blockquote>
  <cite>Dorian Vale, Copper Finch</cite>
</section>

<section class="band news">
  <h2 style="left:128px;top:45px">Most Recent</h2>
  <h2 style="left:589px;top:45px">Featured Blog</h2>
  <div class="recent">
    <div class="item"><div class="thumb" role="img" aria-label="Photo of a laptop keyboard in blue light" style="background:linear-gradient(135deg,#c9d6e8,#5d7aa8)"></div><div><h4>We provide &nbsp;robust cyber security protection</h4><p class="date">MAR 08, 2017</p></div></div>
    <div class="item"><div class="thumb" role="img" aria-label="Photo of a padlock on a keyboard" style="background:linear-gradient(135deg,#e2e4e6,#8a9096)"></div><div><h4>We provide &nbsp;robust cyber security protection</h4><p class="date">MAR 08, 2017</p></div></div>
    <div class="item"><div class="thumb" role="img" aria-label="Photo of a person working at a laptop" style="background:linear-gradient(135deg,#d8cbb8,#6d7f96)"></div><div><h4>We provide &nbsp;robust cyber security protection</h4><p class="date">MAR 08, 2017</p></div></div>
  </div>
  <article class="feature">
    <div class="thumb" role="img" aria-label="Photo of a wooden block with a padlock symbol on a keyboard"></div>
    <p class="date">MAR 08, 2017</p>
    <h4>We provide &nbsp;robust cyber security protection</h4>
    <p>Lorem ipsum dolor sit amet, consectetur adipiscing elit, sed do eiusmod tempor incididunt ut labore et dolore magna aliqua.</p>
  </article>
</section>

<section class="band tweet">
  <span class="bird"></span>
  <p>Lorem ipsum dolor sit amet, consectetur adipiscing elit, sed do eiusmod tempor incididunt ut labore et dolore magna aliqua. Ut enim ad minim veniam, quis nostrud exercitation ullamco laboris nisi ut aliquip ex ea commodo consequat.</p>
</section>

<footer class="band footer">
  <div class="f-brand"><span class="dot"></span><span class="name">VELNASTRA ®</span></div>
  <div class="socials"><i></i><i></i><i></i><i></i></div>
  <div class="f-col sitemap"><h5>SITEMAP</h5><ul><li>Home</li><li>About us</li><li>Services</li><li>Blog</li><li>Contact us</li></ul></div>
  <div class="f-col newsletter"><h5>NEWSLETTER</h5><p>Enter your email address to receive the latest news and notes from our blog</p><div class="field">Enter Your Mail Id</div><span class="btn">SUBSCRIBE</span></div>
  <div class="f-col contact"><h5>CONTACT US</h5><ul>
    <li><svg viewBox="0 0 12 12"><rect x="1" y="1" width="10" height="10" rx="2" fill="#333"/></svg>(555) 014-2290</li>
    <li><svg viewBox="0 0 12 12"><rect x="1" y="3" width="10" height="7" rx="1" fill="#333"/></svg>(555) 014-2291</li>
    <li><svg viewBox="0 0 12 12"><rect x="1" y="2" width="10" height="8" fill="#333"/><path d="M1 2l5 4 5-4" stroke="#fff" fill="none"/></svg>hello@velnastra.example</li>
    <li><svg viewBox="0 0 12 12"><path d="M6 11S2 7 2 4.5a4 4 0 018 0C10 7 6 11 6 11z" fill="#333"/></svg><span>#2868 Lorem ipsum dolor sit<br>amet, consectetur</span></li>
  </ul></div>
  <p class="copy">©2017 Velnastra. All Rights Reserved.</p>
</footer>

</body>
</html>
```